Postcard for Current Clients

We need a postcard to offer a 25% discount for Annual Inspections to current clients that refer us to new clients.
Attached is some info regarding our services
We want to obtain new clients by offering current clients a discounted rate
Our industry is unique and our target market for this project is specific to Property Managers and Building Engineers.

Target Market(s)

Current Clients - Property Managers & Building Engineers

Industry/Entity Type

Window Cleaning

Requirements
Must have
• Red/White/Blue

```html
<!DOCTYPE html>
<html lang="en">
<head>
<meta charset="utf-8">
<title>Referral Postcard – Corwin Safety</title>
<link rel="stylesheet" href="https://fonts.googleapis.com/css2?family=Fjalla+One&family=Lato:wght@400;700&family=Roboto+Condensed:wght@700&display=swap">
<style>
  :root{
    --red:#d7262e;
    --red-dark:#a8161d;
    --blue:#1c4a9c;
    --navy:#1e3f86;
    --ink:#222;
    --panel:#eef1f3;
    --stamp:#5a5a5a;
    --backdrop:#6b4323;
    --white:#fff;
  }
  *{margin:0;padding:0;box-sizing:border-box}
  html,body{width:907px;height:1200px;overflow:hidden}
  body{background:var(--backdrop);position:relative;font-family:"Lato",sans-serif;color:var(--ink)}
  .card{position:absolute;left:95px;width:685px;background:var(--white);overflow:hidden}
  .card--front{top:48px;height:530px}
  .card--back{top:612px;height:528px}
  .card svg.art{position:absolute;left:0;top:0;width:685px}

  .headline{position:absolute;left:14px;top:30px;font-family:"Fjalla One",sans-serif;font-size:34px;line-height:1;color:var(--red)}
  .subhead{position:absolute;left:14px;top:73px;font-size:12px;text-transform:uppercase;color:var(--ink)}

  .lines{position:absolute;font-size:14.5px;line-height:18.3px}
  .lines .ln{display:block;white-space:nowrap;text-align:justify;text-align-last:justify}
  .lines .ln--end{text-align:left;text-align-last:left}
  .intro{left:14px;top:98px;width:396px}
  .question{left:14px;top:16px;width:260px}

  .callout{position:absolute;left:251px;top:258px;font-family:"Roboto Condensed",sans-serif;font-weight:700;line-height:1.1}
  .callout .label{color:var(--navy);font-size:25px}
  .callout .phone{color:var(--red);font-size:25px}

  .brand{position:absolute;display:flex;align-items:center;gap:6px;font-family:"Lato",sans-serif;font-weight:700;color:var(--navy);white-space:nowrap}
  .brand .mark{display:inline-block;background:var(--red)}
  .card--front .brand{left:420px;top:44px;font-size:17px}
  .card--front .brand .mark{width:12px;height:12px}
  .card--back .brand{left:92px;top:236px;font-size:14px}
  .card--back .brand .mark{width:10px;height:10px}

  .discount{position:absolute;left:492px;top:105px;width:170px;height:170px;display:flex;flex-direction:column;align-items:center;justify-content:center;font-family:"Fjalla One",sans-serif;color:var(--white);line-height:.95;text-align:center}
  .discount .pct{font-size:62px}
  .discount .off{font-size:56px}

  .offer{position:absolute;left:17px;top:154px;line-height:1.05}
  .offer .lead{font-family:"Roboto Condensed",sans-serif;font-weight:700;font-size:25px;color:var(--red)}
  .offer .rest{font-family:Arial,sans-serif;font-size:21px;color:#111}
  .contact{position:absolute;left:16px;top:326px;list-style:none;font-size:15px;line-height:20px}
  .contact li{display:flex;gap:7px}
  .contact svg{flex:none;width:10px;height:12px;margin-top:4px}
  .stamp{position:absolute;left:590px;top:15px;width:78px;height:90px;background:var(--stamp)}
</style>
</head>
<body>

<section class="card card--front">
  <svg class="art" height="530" viewBox="0 0 685 530">
    <defs>
      <radialGradient id="badge" cx="40%" cy="35%" r="70%">
        <stop offset="0" stop-color="#e8383f"/><stop offset="1" stop-color="#a8161d"/>
      </radialGradient>
      <linearGradient id="site" x1="0" y1="0" x2="1" y2="1">
        <stop offset="0" stop-color="#9fb7cf"/><stop offset=".6" stop-color="#c6d2dc"/><stop offset="1" stop-color="#f4f6f8"/>
      </linearGradient>
      <linearGradient id="detail" x1="0" y1="0" x2="1" y2="1">
        <stop offset="0" stop-color="#9a9a98"/><stop offset="1" stop-color="#c8c8c4"/>
      </linearGradient>
    </defs>
    <path d="M360 0 C380 40 430 90 520 115" fill="none" stroke="var(--blue)" stroke-width="10"/>
    <path d="M380 0 C400 40 450 85 530 108" fill="none" stroke="var(--red)" stroke-width="6"/>
    <path d="M590 260 C640 300 660 330 685 350" fill="none" stroke="var(--blue)" stroke-width="9"/>
    <path d="M600 275 C640 310 665 340 685 360" fill="none" stroke="var(--red)" stroke-width="5"/>
    <path role="img" aria-label="Photo of crew on a window cleaning platform high above the city" fill="url(#site)"
      d="M0 272 C120 268 240 300 330 360 C400 405 460 420 510 420 L560 530 L0 530 Z"/>
    <path d="M0 264 C120 258 240 292 330 352 C400 398 460 412 510 412" fill="none" stroke="var(--red)" stroke-width="6"/>
    <path d="M0 275 C120 270 240 302 330 362 C400 405 460 420 500 420" fill="none" stroke="var(--blue)" stroke-width="3"/>
    <path d="M620 465 C650 480 670 495 685 505" fill="none" stroke="var(--red)" stroke-width="5"/>
    <circle role="img" aria-label="Close-up photo of a roof anchor inspection" cx="565" cy="397" r="80" fill="url(#detail)"/>
    <circle cx="565" cy="397" r="84" fill="none" stroke="var(--blue)" stroke-width="8"/>
    <circle cx="577" cy="190" r="87" fill="url(#badge)"/>
  </svg>

  <h1 class="headline">OFFERING NEW CLIENTS</h1>
  <p class="subhead">A discounted rate for annual inspections!</p>
  <p class="lines intro">
    <span class="ln">When it comes to exterior building maintenance systems,</span>
    <span class="ln">Corwin Safety is an industry specialist. Our turnkey services</span>
    <span class="ln">include: design, engineering, installation, retrofitting,</span>
    <span class="ln">inspections, testing, certification, training, and OPOS docu-</span>
    <span class="ln">mentation. We specialize in bringing your existing exterior</span>
    <span class="ln">building maintenance system, commonly referred to a</span>
    <span class="ln ln--end">window cleaning systems, into compliance</span>
    <span class="ln ln--end">with OSHA safety standards.</span>
  </p>
  <div class="brand"><span class="mark"></span>Corwin Safety</div>
  <div class="discount"><span class="pct">25%</span><span class="off">OFF</span></div>
  <p class="callout"><span class="label">Call today</span><br><span class="phone">(800) 555-0142</span></p>
</section>

<section class="card card--back">
  <svg class="art" height="528" viewBox="0 0 685 528">
    <defs>
      <linearGradient id="city" x1="0" y1="0" x2="1" y2="1">
        <stop offset="0" stop-color="#6c7480"/><stop offset="1" stop-color="#b9bfc6"/>
      </linearGradient>
    </defs>
    <path d="M0 0 L345 0 C345 80 330 150 292 190 C250 225 120 232 0 232 Z" fill="var(--panel)"/>
    <path d="M345 0 C345 80 330 150 292 190 C250 225 120 232 0 232" fill="none" stroke="var(--red)" stroke-width="5"/>
    <path d="M0 236 C80 244 140 274 170 302 C210 292 250 272 280 257" fill="none" stroke="var(--blue)" stroke-width="8"/>
    <path d="M0 246 C80 254 140 284 175 312 C215 300 255 280 285 264" fill="none" stroke="var(--red)" stroke-width="5"/>
    <path d="M275 250 C310 320 320 380 315 435" fill="none" stroke="var(--blue)" stroke-width="8"/>
    <path d="M265 255 C298 320 306 380 300 435" fill="none" stroke="var(--red)" stroke-width="4"/>
    <path d="M348 0 L348 28" stroke="var(--blue)" stroke-width="8"/>
    <circle role="img" aria-label="Aerial photo of downtown high-rise towers" cx="352" cy="90" r="60" fill="url(#city)"/>
    <circle cx="352" cy="90" r="65" fill="none" stroke="var(--blue)" stroke-width="6"/>
  </svg>

  <p class="lines question">
    <span class="ln">Is your building in compliance with</span>
    <span class="ln">OSHA Safety Standards? Providing a</span>
    <span class="ln">safe work environment can be a diffi-</span>
    <span class="ln">cult task. We offer a FREE evaluation</span>
    <span class="ln">of your exterior building maintenance</span>
    <span class="ln">(window cleaning) system. In this</span>
    <span class="ln ln--end">evaluation you will receive:</span>
  </p>
  <p class="offer"><span class="lead">TAKE ADVANTAGE OF</span><br><span class="rest">THIS SPECIAL OFFER!</span></p>
  <div class="brand"><span class="mark"></span>Corwin Safety</div>
  <ul class="contact">
    <li><svg viewBox="0 0 10 12"><path d="M5 0a4 4 0 0 1 4 4c0 3-4 8-4 8S1 7 1 4a4 4 0 0 1 4-4z" fill="var(--red)"/><circle cx="5" cy="4" r="1.5" fill="#fff"/></svg><span>1280 Harbor Point Way, Ste. B<br>Oakdale, CA 95361</span></li>
    <li><svg viewBox="0 0 10 12"><rect x="0" y="1" width="10" height="10" rx="2" fill="var(--red)"/><path d="M3 3l1.5 0 .5 2-1 .8a4 4 0 0 0 1.8 1.8l.8-1 2 .5 0 1.5C5 9 2 6 3 3z" fill="#fff"/></svg>(800) 555-0142</li>
    <li><svg viewBox="0 0 10 12"><rect x="0" y="3" width="10" height="7" fill="var(--red)"/><path d="M0 3l5 4 5-4" fill="none" stroke="#fff" stroke-width="1"/></svg>info@corwinsafety.com</li>
    <li><svg viewBox="0 0 10 12"><circle cx="5" cy="6" r="4.5" fill="var(--red)"/><path d="M.5 6h9M5 1.5v9" stroke="#fff" stroke-width=".7"/></svg>corwinsafety.com</li>
  </ul>
  <div class="stamp"></div>
</section>

</body>
</html>
```